K5Lesson WebSite

an educational website about tutoring, client will be surfing this site looking for a tutor, please see the attached images because the contains exactly what we need.
Updates

Project Deadline Extended Reason: something went wrong with the uploaded files, we are very sorry.thank you PixelBazaar for the 5 days extension.now there is a 3 images describing the content of the three pages.good luck Added Friday, August 5, 2016

Target Market(s)

everyone

Industry/Entity Type

Education

Number of Pages Required

3 page

Font styles to use
Other font styles liked:
• something looks good in Arabic and english like "Droid Arabic Kufi"

Requirements
Must have
• the logo we attached, responsive design, simple, also try as much as you can Centering texts and layout because this website will have an Arabic version, Arabic is a Right-to-Left Language.
• a change language button,
Nice to have
• educational gestures.
• Centered texts and layout because this website will have an Arabic version, Arabic is a Right-to-Left Language.
• we have a web designer and we can download any template and add our logo and text to it, but.....
• we need creativity, so please stick to the contents in the images we attached, we need something very simple, more like a varnel home page with little touch of filtering fields like the 5 dropdownlist and the gender selection buttons.
• try not to go far away from the contents we specified in the images, use less images or dont use images at all, try not to make the client scroll down,
Should not have
• too much colors or noisy layout or heavy media

```html
<!DOCTYPE html>
<html lang="en">
<head>
<meta charset="utf-8">
<title>K5Lesson — Home</title>
<link href="https://fonts.googleapis.com/css2?family=Ubuntu:wght@400;500;700&family=Signika:wght@300;400&display=swap" rel="stylesheet">
<style>
:root{
  --brand:#1aa3e0;
  --deep:#0f72bb;
  --ink:#1566b0;
  --text-soft:#2a9fd8;
  --white:#ffffff;
  --line:#d9dde2;
  --green:#7dc243;
  --dark:#1d2b3a;
}
*{margin:0;padding:0;box-sizing:border-box}
html,body{width:849px;height:1200px;overflow:hidden;background:var(--white)}
body{position:relative;font-family:"Ubuntu",sans-serif;color:var(--ink)}
.abs{position:absolute}

.brand-name{left:100px;top:44px;width:146px;font-size:24px;font-weight:500;color:var(--ink);display:flex;align-items:center;gap:6px;letter-spacing:-0.5px;white-space:nowrap}
.brand-name .mark{width:24px;height:24px;background:var(--brand);border-radius:4px;flex:none}

.main-nav{left:254px;top:34px;width:504px;height:52px;background:var(--brand);border-radius:9px;display:flex;align-items:center;justify-content:space-around;padding:0 6px}
.main-nav a{color:var(--white);text-decoration:none;font-size:13.5px;font-weight:500;padding:0 12px;border-left:1px solid rgba(255,255,255,.8);line-height:32px}
.main-nav a:first-child{border-left:none}

.hero{left:89px;top:102px;width:671px;height:343px;background:linear-gradient(160deg,#cfd3d6 0%,#a7a49d 35%,#6f6a63 70%,#4a4c4d 100%)}
.hero-caption{left:534px;top:202px;width:208px;height:102px;background:rgba(40,130,200,.62);padding:8px 12px;color:var(--white)}
.hero-caption h2{font-family:"Ubuntu",sans-serif;font-weight:400;font-size:26px;letter-spacing:.3px;line-height:1.1}
.hero-caption p{font-family:"Signika",sans-serif;font-weight:300;font-size:12.5px;line-height:16px;margin-top:7px;width:140px}
.hero-arrow{top:258px}

.welcome-title{left:93px;top:469px;font-size:21px;font-weight:700;letter-spacing:.6px;color:var(--ink)}
.welcome-sub{left:93px;top:496px;font-size:19px;font-weight:700;line-height:25px;color:var(--brand);width:400px;letter-spacing:-.3px}
.welcome-copy{left:92px;top:545px;font-family:"Signika",sans-serif;font-weight:300;font-size:12px;line-height:20.7px;color:var(--text-soft)}

.tutors-title{left:93px;top:653px;font-size:19px;font-weight:700;color:var(--ink);letter-spacing:-.3px}
.tutors-photo{left:89px;top:682px;width:151px;height:93px;background:linear-gradient(90deg,#7f8f7d,#40564a 50%,#8a8e86)}
.tutors-copy{left:254px;top:691px;font-family:"Signika",sans-serif;font-weight:300;font-size:12px;line-height:19.8px;color:var(--text-soft);letter-spacing:-.2px}

.divider{left:517px;top:512px;width:2px;height:272px;background:var(--line)}

.staff-title{left:562px;top:465px;font-size:24px;font-weight:500;color:var(--ink);letter-spacing:.3px}
.staff-row{left:563px;width:210px;display:flex;gap:20px}
.staff-photo{width:65px;height:60px;flex:none}
.staff-info h4{font-size:9.5px;font-weight:700;color:var(--ink);margin-top:9px}
.staff-info p{font-family:"Signika",sans-serif;font-weight:300;font-size:7px;line-height:10.3px;color:var(--text-soft)}

.btn{display:flex;align-items:center;justify-content:center;background:var(--deep);color:var(--white);font-size:13.5px;font-weight:700;border-radius:4px;width:115px;height:38px;letter-spacing:-.3px}

.programmes{left:89px;top:858px;width:671px;height:203px;background:var(--deep);color:var(--white)}
.programmes h2{position:absolute;left:0;width:408px;top:24px;text-align:center;font-size:24px;font-weight:500}
.programmes p{position:absolute;left:0;width:408px;top:65px;text-align:center;font-family:"Signika",sans-serif;font-weight:300;font-size:12px;line-height:14.6px}
.programmes .frame{position:absolute;left:414px;top:28px;width:208px;height:144px;background:var(--white);padding:5px}
.programmes .frame div{width:100%;height:100%;background:linear-gradient(135deg,#d9d2c4,#a9947a 45%,#5f6d86)}

.foot-head{top:1077px;font-size:16px;font-weight:400;color:var(--ink)}
.foot-list{top:1104px;list-style:none;font-size:9.5px;color:var(--ink)}
.foot-list li{height:21px;display:flex;align-items:flex-start;gap:5px}
.foot-list li::before{content:"";width:0;height:0;border-top:4px solid transparent;border-bottom:4px solid transparent;border-left:5px solid var(--ink);margin-top:1px}
.follow-item{left:343px;display:flex;align-items:center;gap:6px;font-size:10px;color:var(--ink)}
.follow-item span.ico{width:20px;height:20px;background:var(--brand);border-radius:2px}

.news-input{left:582px;top:1098px;width:164px;height:20px;background:var(--brand);border-radius:2px}
.unsub{left:583px;top:1133px;font-size:10px;font-weight:500;color:var(--dark)}
.subscribe{left:679px;top:1128px;width:66px;height:23px;background:var(--green);color:var(--white);font-size:10px;font-weight:500;display:flex;align-items:center;justify-content:center;border-radius:2px}
.copyright{left:583px;top:1164px;font-size:10px;font-weight:500;color:var(--dark)}
</style>
</head>
<body>

<div class="abs brand-name"><span class="mark"></span>K5Lesson</div>

<nav class="abs main-nav">
  <a href="#">HOME</a><a href="#">ACADEMICS</a><a href="#">PROGRAMMES</a><a href="#">CALENDER</a><a href="#">CONTACTS</a>
</nav>

<div class="abs hero" role="img" aria-label="Group photo of smiling tutors and students holding books in a classroom"></div>
<div class="abs hero-caption">
  <h2>LOREM IPSUM</h2>
  <p>Is simply dummy text of the printing and typesetting industry</p>
</div>
<svg class="abs hero-arrow" style="left:120px" width="22" height="34" viewBox="0 0 22 34"><polyline points="18,3 5,17 18,31" fill="none" stroke="#fff" stroke-width="4"/></svg>
<svg class="abs hero-arrow" style="left:706px" width="22" height="34" viewBox="0 0 22 34"><polyline points="4,3 17,17 4,31" fill="none" stroke="#fff" stroke-width="4"/></svg>

<h1 class="abs welcome-title">WELCOME TO OUR WEBSITE</h1>
<h2 class="abs welcome-sub">We are among the leading research and teaching websites</h2>
<p class="abs welcome-copy">Lorem Ipsum has been the industry's standard dummy text ever<br>since the 1500s, when an unknown printer took a galley<br>of type and scrambled it to make a type specimen book.<br>It has survived not only five centuries</p>

<h2 class="abs tutors-title">What we&nbsp; want are tutors</h2>
<div class="abs tutors-photo" role="img" aria-label="Three tutors standing in front of a chalkboard"></div>
<p class="abs tutors-copy">An educational website about tutoring,<br>client will be surfing this site looking for a tutor<br>An educational website about tutoring,<br>client will be surfing this site looking for a tutor</p>

<div class="abs divider"></div>

<h2 class="abs staff-title">Our staff</h2>
<div class="abs staff-row" style="top:498px">
  <div class="staff-photo" role="img" aria-label="Staff portrait" style="background:linear-gradient(#5f7d63,#c6a58e)"></div>
  <div class="staff-info"><h4>Marisol Dunleavy</h4><p>It was popularised in the 1960s<br>the release of Letraset sheets<br>containing Lorem Ipsum passage</p></div>
</div>
<div class="abs staff-row" style="top:572px">
  <div class="staff-photo" role="img" aria-label="Staff portrait" style="background:linear-gradient(#2f3c3a,#a4785e)"></div>
  <div class="staff-info"><h4>Marisol Dunleavy</h4><p>It was popularised in the 1960s<br>the release of Letraset sheets<br>containing Lorem Ipsum passage</p></div>
</div>
<div class="abs staff-row" style="top:646px">
  <div class="staff-photo" role="img" aria-label="Staff portrait" style="background:linear-gradient(#eee,#b2623e)"></div>
  <div class="staff-info"><h4>Marisol Dunleavy</h4><p>It was popularised in the 1960s<br>the release of Letraset sheets<br>containing Lorem Ipsum passage</p></div>
</div>
<div class="abs staff-row" style="top:722px">
  <div class="staff-photo" role="img" aria-label="Staff portrait" style="background:linear-gradient(#34413f,#8a5f4a 60%,#1f2a33)"></div>
  <div class="staff-info"><h4>Marisol Dunleavy</h4><p>It was popularised in the 1960s<br>the release of Letraset sheets<br>containing Lorem Ipsum passage</p></div>
</div>

<a class="abs btn" style="left:107px;top:805px">READ MORE</a>
<a class="abs btn" style="left:531px;top:802px">READ MORE</a>

<section class="abs programmes">
  <h2>PROGRAMMES</h2>
  <p>It is a long established fact that<br>a reader will be distracted by the readable<br>content of a page when looking at its layout.<br>The point of using Lorem Ipsum is that it has<br>a more-or-less normal distribution of letters,<br>as opposed to using 'Content here, content here'<br>, making it look like readable English.</p>
  <div class="frame"><div role="img" aria-label="Teacher helping young children at a classroom table"></div></div>
</section>

<h3 class="abs foot-head" style="left:103px">Links</h3>
<ul class="abs foot-list" style="left:103px"><li>Catalog</li><li>Solutions</li><li>Guarantee</li></ul>

<h3 class="abs foot-head" style="left:223px">Join In</h3>
<ul class="abs foot-list" style="left:223px"><li>Sign Up</li><li>Forums</li><li>Promotions</li></ul>

<h3 class="abs foot-head" style="left:343px;top:1075px">Follow Us</h3>
<div class="abs follow-item" style="top:1105px"><span class="ico"></span></div>
<div class="abs follow-item" style="top:1128px"><span class="ico"></span>Chirper</div>

<h3 class="abs foot-head" style="left:581px">Newsletter</h3>
<div class="abs news-input"></div>
<div class="abs unsub">unsubscribe</div>
<div class="abs subscribe">subscribe ›</div>
<div class="abs copyright">Lessa@2016| privacy policy</div>

</body>
</html>
```